Painting Company Business Card

Brightwell Painting needs a new business card. See attachments for our logo and current card as an example.
We want to utilize the same colors in the logo, and keep all the information that is currently on it. Just need an updated and modern design.
We are open to loosing the Association Logos if it means a better design.
We are also entertaining a spot for a picture of a headshot of the person listed on the card. Head shot can be finished later.

```html
<!DOCTYPE html>
<html lang="en">
<head>
<meta charset="utf-8">
<title>Brightwell Painting – Business Card</title>
<link href="https://fonts.googleapis.com/css2?family=Arimo:wght@400;700&display=swap" rel="stylesheet">
<style>
  :root{
    --bg:#a99d8b;
    --card:#ffffff;
    --brown:#734a45;
    --green:#4b5240;
    --tan:#e9e1d5;
    --text:#6b6b6b;
    --name:#666666;
    --badge:#c8ccd4;
    --badge-blue:#2f5a9e;
  }
  *{margin:0;padding:0;box-sizing:border-box}
  html,body{width:1200px;height:1200px;overflow:hidden;background:var(--bg)}
  body{position:relative;font-family:"Arimo",Arial,sans-serif}
  .card{position:absolute;left:247px;width:705px;height:392px;background:var(--card);overflow:hidden;box-shadow:0 3px 6px rgba(0,0,0,.15)}
  .card--front{top:144px}
  .card--back{top:648px}
  .paint-art{position:absolute}
  .paint-art--brown-stroke{background:var(--brown)}
  .paint-art--green-stroke{background:var(--green)}
  .paint-art--brown-roller{background:linear-gradient(to bottom,var(--tan) 0%,var(--tan) 30%,var(--brown) 42%,var(--brown) 100%)}
  .paint-art--green-roller{background:linear-gradient(to bottom,var(--tan) 0%,var(--tan) 30%,var(--green) 42%,var(--green) 100%)}
  .holder{position:absolute;left:0;right:0;text-align:center;color:var(--name)}
  .holder__name{top:120px;font-size:35px;font-weight:700;transform:translateX(-12px)}
  .holder__title{top:163px;font-size:24px;font-weight:400;color:var(--text);transform:translateX(-14px)}
  .contact{position:absolute;left:235px;list-style:none;top:305px;transform:translateY(-82px)}
  .contact__item{display:flex;align-items:center;height:34.5px;font-size:18px;color:var(--text)}
  .contact__icon{width:22px;height:22px;margin-right:18px;flex:none}
  .brand{position:absolute;left:190px;width:310px;top:72px;text-align:center;color:var(--green);font-weight:700;font-size:40px;line-height:48px;letter-spacing:1px}
  .badges{position:absolute;left:252px;top:195px;width:182px;display:grid;grid-template-columns:repeat(3,50px);gap:16px;justify-content:space-between}
  .badge{height:38px;border-radius:4px;background:var(--badge)}
  .badge--blue{background:var(--badge-blue)}
  .badge--wide{height:26px;margin-top:6px}
  .services{position:absolute;left:0;right:0;top:319px;text-align:center;font-size:20px;line-height:28px;color:var(--text);transform:translateX(-15px)}
</style>
</head>
<body>

<section class="card card--front">
  <div class="paint-art paint-art--brown-stroke" style="left:225px;top:0;width:86px;height:77px" role="img" aria-label="Brown paint stroke dripping from the top edge"></div>
  <div class="paint-art paint-art--green-stroke" style="left:393px;top:0;width:87px;height:64px" role="img" aria-label="Green paint stroke dripping from the top edge"></div>
  <div class="paint-art paint-art--brown-roller" style="left:57px;top:40px;width:87px;height:352px" role="img" aria-label="Paint roller rolling a brown stripe down the card"></div>
  <div class="paint-art paint-art--green-roller" style="left:562px;top:40px;width:87px;height:352px" role="img" aria-label="Paint roller rolling a green stripe down the card"></div>

  <h1 class="holder holder__name">Daniel Harper</h1>
  <p class="holder holder__title">Quality Manager</p>
  <ul class="contact">
    <li class="contact__item">
      <svg class="contact__icon" viewBox="0 0 24 24"><circle cx="12" cy="12" r="11" fill="var(--brown)"/><path d="M8.5 6.5l2 2.5-1.2 1.5c.8 1.8 2.2 3.2 4 4l1.5-1.2 2.5 2-1.2 2c-4.5-.3-8.6-4.4-8.9-8.9z" fill="#fff"/></svg>
      555-014-2763
    </li>
    <li class="contact__item">
      <svg class="contact__icon" viewBox="0 0 24 24"><rect x="1" y="5" width="22" height="14" fill="var(--brown)"/><path d="M1 5l11 8 11-8" fill="none" stroke="#fff" stroke-width="1.6"/></svg>
      daniel.brightwell@mail.com
    </li>
    <li class="contact__item">
      <svg class="contact__icon" viewBox="0 0 24 24" fill="none" stroke="var(--brown)" stroke-width="1.3"><circle cx="12" cy="12" r="10"/><ellipse cx="12" cy="12" rx="4.5" ry="10"/><path d="M2 12h20M4 7h16M4 17h16"/></svg>
      www.brightwellpainting.com
    </li>
  </ul>
</section>

<section class="card card--back">
  <div class="paint-art paint-art--brown-stroke" style="left:57px;top:0;width:87px;height:92px" role="img" aria-label="Brown paint stroke dripping from the top edge"></div>
  <div class="paint-art paint-art--green-stroke" style="left:562px;top:0;width:87px;height:62px" role="img" aria-label="Green paint stroke dripping from the top edge"></div>
  <div class="paint-art paint-art--brown-roller" style="left:57px;top:140px;width:87px;height:252px" role="img" aria-label="Paint roller rolling a brown stripe up from the bottom edge"></div>
  <div class="paint-art paint-art--green-roller" style="left:562px;top:93px;width:87px;height:299px" role="img" aria-label="Paint roller rolling a green stripe up from the bottom edge"></div>

  <div class="brand">BRIGHTWELL<br>PAINTING</div>
  <div class="badges" aria-label="Association memberships">
    <div class="badge badge--blue"></div>
    <div class="badge"></div>
    <div class="badge"></div>
    <div class="badge badge--wide"></div>
    <div class="badge badge--wide badge--blue"></div>
    <div class="badge badge--wide"></div>
  </div>
  <p class="services">Exterior Painting, Interior Painting<br>Carpentry, Drywall</p>
</section>
</body>
</html>
```